Business Card Design

I am a video director/cameraman and photographer. I cover documentaries, corporate, government departments, educational and non profits. They could be on Tv, Vidzio or DVD to 10 or 10 thousand ppl. Some have been seen worldwide and won international awards.
I regard myself as bold and saturated...as in I want strong ideas of substance to come through in a film and that the info is valid, interesting and saturates the mind without it being geeky boring.
Need a great logo and layout for cards. My name is Lionel Brastow and my company is TV Media Productions.

Must have company name, my name, email, website, phone and type of films I do. I'll supply additional info for the back- which will be companies I have filmed for.

Attach image shows I like the boxes/icons idea but am open to yr ideas...Roar on!
Updates

Project Deadline Extended
Reason: I am charged by your designs. This is the first time I have used ths type of service and getting to know you guys is very good value for me. Please keep your creative spirit in this. I want a contemporary logo. Some have shown the way forward and a few need to show a clean, current looking image of my attitude by way of log and design. Thx to you all Leo

Industry/Entity Type

Government

```html
<!DOCTYPE html>
<html lang="en">
<head>
<meta charset="utf-8">
<title>TV Media Productions – Business Card</title>
<link href="https://fonts.googleapis.com/css2?family=Lato:wght@400;700;900&display=swap" rel="stylesheet">
<style>
  :root {
    --backdrop: #e9e6e1;
    --card: #2a2a2a;
    --card-seam: #1e1e1e;
    --green: #3a9a44;
    --ink: #f2f2f2;
  }
  * { margin: 0; padding: 0; box-sizing: border-box; }
  html, body {
    width: 1200px; height: 800px; overflow: hidden;
    background: var(--backdrop);
    font-family: "Lato", sans-serif;
  }
  .canvas { position: relative; width: 1200px; height: 800px; }

  .card {
    position: absolute; left: 222px; width: 553px;
    background: var(--card); color: var(--ink);
  }
  .card--front { top: 98px; height: 324px; }
  .card--back { top: 422px; height: 328px; border-top: 2px solid var(--card-seam); }

  /* Front */
  .front-brand {
    position: absolute; left: 0; right: 0; top: 112px;
    display: flex; align-items: center; justify-content: center; gap: 18px;
  }
  .brand-ring {
    width: 64px; height: 64px; border-radius: 50%;
    border: 6px solid var(--green); flex: none;
  }
  .front-brand .brand-name { font-size: 32px; white-space: nowrap; }
  .brand-name { color: var(--green); font-weight: 900; letter-spacing: 0.5px; }
  .tagline {
    position: absolute; left: 0; right: 0; top: 260px;
    text-align: center; font-size: 17px; letter-spacing: 0.2px;
  }

  /* Back */
  .back-brand {
    position: absolute; left: 36px; top: 44px;
    display: flex; align-items: center; gap: 14px;
  }
  .back-brand .brand-ring { width: 96px; height: 96px; border-width: 6px; }
  .back-brand .brand-name {
    font-size: 24px; line-height: 27px; width: 170px;
  }
  .back-brand .brand-name span { display: block; }

  .person { position: absolute; left: 356px; top: 60px; }
  .person-name { color: var(--green); font-weight: 700; font-size: 18px; line-height: 20px; margin-bottom: 1px; }
  .person-role { font-size: 15px; line-height: 17.5px; }

  .contact { position: absolute; left: 36px; top: 240px; list-style: none; }
  .contact li {
    display: flex; align-items: center; gap: 7px;
    font-size: 15px; line-height: 19.5px;
  }
  .contact svg { width: 14px; height: 14px; fill: var(--green); flex: none; }

  .services { position: absolute; left: 357px; top: 224px; list-style: none; }
  .services li { font-size: 15px; line-height: 19.5px; }
</style>
</head>
<body>
<main class="canvas">
  <section class="card card--front">
    <div class="front-brand">
      <span class="brand-ring"></span>
      <span class="brand-name">TV Media Productions</span>
    </div>
    <p class="tagline">Supporting Your Production to Maximum Exposure</p>
  </section>

  <section class="card card--back">
    <div class="back-brand">
      <span class="brand-ring"></span>
      <span class="brand-name"><span>TV Media</span><span>Productions</span></span>
    </div>

    <div class="person">
      <p class="person-name">Lionel Brastow</p>
      <p class="person-role">Video Director</p>
      <p class="person-role">Cameraman</p>
      <p class="person-role">Photographer</p>
    </div>

    <ul class="contact">
      <li>
        <svg viewBox="0 0 14 14" aria-hidden="true"><path d="M4 0h6a1 1 0 0 1 1 1v12a1 1 0 0 1-1 1H4a1 1 0 0 1-1-1V1a1 1 0 0 1 1-1zm0.5 2v8h5V2zm2.5 9.2a0.9 0.9 0 1 0 0 1.8a0.9 0.9 0 0 0 0-1.8z"/></svg>
        123 456 7890
      </li>
      <li>
        <svg viewBox="0 0 14 14" aria-hidden="true"><path d="M0 3h14v8H0zm1.2 1.2v0.3L7 8l5.8-3.5v-0.3z"/></svg>
        lionel@tvmediaproductions.com
      </li>
      <li>
        <svg viewBox="0 0 14 14" aria-hidden="true"><path d="M7 0.5a6.5 6.5 0 1 0 0 13a6.5 6.5 0 0 0 0-13zM4 3.5l2 1-0.5 2 1.5 1.5-1 2.5-2-2-1-2.5zm5 0.5l2 1.5 0.5 3-1.5 1.5-1-2-1-1.5z"/></svg>
        www.tvmediaproductions.com
      </li>
    </ul>

    <ul class="services">
      <li>Documentaries</li>
      <li>Corporate</li>
      <li>TVC, government</li>
      <li>Educational and Non Profits.</li>
    </ul>
  </section>
</main>
</body>
</html>
```